Brisk Tide needs a web page for E-commerce site

Small startup business looking for a custom website for my New Saltwater apparel Co.

COMPANY OVERVIEW

Brisk Tide was founded In Mont Belvieu, Tx, right on the heart of pelican cove.

Brisk Tide is the adrenaline, sweat pumping moment you find yourself setting the hook on a monster fish. This is the moment when all your senses come to life as you work to land that trophy, and after a grueling fight when your hi-fiving your fishing buddies...It's that moment... when the waters and the air around you are Brisk Sweet....All or Nothing...pure Addiction......This is BRISK TIDE

Looking for a sharp clean sexy web page for my ecommerce page

I like the look of black background websites.

www.brisktidegear.example
Updates

I am using bigcommerce as my host site if that means anything to y'all

Thank you all for the submissions! There were some great ones!  I will have more projects in the future. thanks again

Target Market(s)

inshore/offshore fishing, saltwater enthusiast

Industry/Entity Type

Business

Requirements
Must have
• logo's

inshore/offshore fishing appeal

compatible with bigcommerce site

```html
<!DOCTYPE html>
<html lang="en">
<head>
<meta charset="utf-8">
<title>Brisk Tide – Saltwater Apparel</title>
<link href="https://fonts.googleapis.com/css2?family=Schoolbell&family=Arimo:wght@400;700&display=block" rel="stylesheet">
<style>
:root{
  --bg:#1f1f1f;
  --bg-dark:#161616;
  --panel:#111;
  --orange:#f7901e;
  --white:#fff;
  --muted:#8a8a8a;
  --light:#d8d8d8;
  --card:#fff;
  --btn:#222;
  --teal:#1f9a9c;
  --script:"Schoolbell","Comic Sans MS",cursive;
}
*{box-sizing:border-box;margin:0;padding:0}
html,body{width:1148px;height:1200px;overflow:hidden}
body{background:var(--bg);font-family:"Arimo",Arial,sans-serif;color:var(--white);position:relative}
.abs{position:absolute}
.top-links{top:13px;right:151px;font-size:11px;color:var(--light);display:flex;gap:8px}
.top-links .accent{color:var(--orange);font-weight:700}
.brand{left:156px;top:38px;font-family:var(--script);font-size:44px;color:var(--orange);display:flex;align-items:center;gap:12px;line-height:1}
.brand .dot{width:14px;height:14px;border-radius:50%;background:var(--orange)}
.search{left:674px;top:38px;width:150px;height:26px;background:#0e0e0e;border:1px solid #333}
.search svg{position:absolute;right:8px;top:5px}
.cart{left:836px;top:38px;width:162px;height:26px;background:#0e0e0e;display:flex;align-items:center;gap:8px;padding-left:12px;font-size:11px;color:var(--light)}
.cart b{color:var(--orange)}
.cart u{margin-left:10px;font-size:10px}
.main-nav{top:75px;left:524px;width:466px;display:flex;justify-content:space-between;font-size:15px;font-weight:700;color:var(--orange)}
.slider-frame{left:142px;top:115px;width:866px;height:405px;background:#2a2a2a;box-shadow:0 0 12px #000}
.slide{left:150px;top:125px;width:847px;height:385px;background:
  radial-gradient(ellipse 150px 130px at 30% 45%,rgba(31,154,156,.45),rgba(31,154,156,0) 70%),
  radial-gradient(ellipse 230px 250px at 30% 55%,#fafafa 0%,rgba(250,250,250,0) 75%),
  radial-gradient(ellipse 240px 260px at 72% 55%,#fbfbfb 0%,rgba(250,250,250,0) 75%),
  linear-gradient(#dcdcdc,#bdbdbd)}
.slide-caption{left:150px;top:457px;width:847px;height:53px;background:rgba(40,40,40,.75);font-family:var(--script);font-size:34px;line-height:37px;padding:8px 20px;color:var(--white)}
.arrow{top:304px}
.section-title{font-size:16px;font-weight:400;left:150px;top:538px}
.decal-ad{left:151px;top:574px;width:202px;height:252px;background:var(--panel);padding:12px}
.decal-ad .inner{border:2px dotted #666;height:100%;display:flex;flex-direction:column;align-items:center;justify-content:center;font-family:var(--script);color:var(--orange);text-align:center}
.decal-ad .name{font-size:32px;line-height:1.1}
.decal-ad .word{font-size:36px;color:var(--white);line-height:1.1}
.decal-ad .cta{font-family:"Arimo",Arial,sans-serif;font-weight:700;font-size:17px;color:var(--white);text-decoration:underline;margin-top:16px}
.product{top:574px;height:252px;background:var(--card);text-align:center;color:#222}
.product .shot{margin:22px auto 0;width:166px;height:96px;border-radius:6px}
.product h3{font-family:var(--script);font-weight:400;font-size:17px;margin-top:14px;line-height:1.2}
.product .price{font-family:var(--script);color:var(--orange);font-size:17px;line-height:1.2}
.product .buy{display:inline-block;margin-top:18px;background:var(--btn);color:var(--white);font-weight:700;font-size:13px;padding:9px 22px}
.welcome-title{left:154px;top:848px;font-family:var(--script);font-weight:400;font-size:25px;line-height:1.1}
.welcome-text{left:156px;top:890px;width:840px;font-size:11.6px;line-height:18.5px;color:var(--muted)}
.news-title{left:152px;top:994px;font-family:var(--script);font-weight:400;font-size:25px;line-height:1.1}
.news-form{left:150px;top:1039px;width:372px;height:36px;background:#0a0a0a;display:flex}
.news-form span{flex:1;font-size:11px;font-style:italic;color:#777;padding:12px 14px}
.news-form b{width:88px;background:var(--orange);font-size:13px;display:flex;align-items:center;justify-content:center}
.follow-title{left:588px;top:994px;font-family:var(--script);font-weight:400;font-size:25px;line-height:1.1}
.social{top:1042px;display:flex;align-items:center;gap:14px;font-size:13px;color:var(--light)}
.social i{width:26px;height:26px;display:block;border-radius:3px}
.footer{left:0;top:1111px;width:1148px;height:89px;background:var(--bg-dark)}
.foot-links{left:149px;font-size:10px;font-weight:700;color:var(--light);display:flex;gap:8px}
.foot-brand{left:822px;top:1130px;font-family:var(--script);font-size:30px;color:var(--orange);line-height:1}
.copy{left:878px;top:1174px;font-size:10px;font-weight:700;color:var(--light)}
</style>
</head>
<body>
<nav class="top-links abs"><span>CONTACT US</span>|<span>SUBSCRIBE</span>|<span>MY ACCOUNT</span>|<span class="accent">CREATE ACCOUNT</span></nav>
<div class="brand abs"><span class="dot"></span>Brisk Tide</div>
<div class="search abs"><svg width="16" height="16" viewBox="0 0 16 16"><circle cx="6.5" cy="6.5" r="5" fill="none" stroke="#777" stroke-width="2"/><line x1="10" y1="10" x2="15" y2="15" stroke="#777" stroke-width="2"/></svg></div>
<div class="cart abs"><svg width="18" height="14" viewBox="0 0 18 14"><path d="M1 1h3l2 8h9l2-6H5" fill="none" stroke="#bbb" stroke-width="1.5"/><circle cx="7" cy="12" r="1.4" fill="#bbb"/><circle cx="14" cy="12" r="1.4" fill="#bbb"/></svg><span><b>10</b> (items)</span><u>VIEW CART</u></div>
<nav class="main-nav abs"><span>COLLECTIONS</span><span>SHIRTS</span><span>SHORTS</span><span>HEADWEAR</span><span>DECALS</span></nav>

<div class="slider-frame abs"></div>
<div class="slide abs" role="img" aria-label="White trout shirt with teal fish print, shown from back and front on a light paper backdrop"></div>
<div class="slide-caption abs">Trout Shirt White</div>
<svg class="arrow abs" style="left:108px" width="16" height="28" viewBox="0 0 16 28"><path d="M13 2L3 14l10 12" fill="none" stroke="#777" stroke-width="4"/></svg>
<svg class="arrow abs" style="left:1024px" width="16" height="28" viewBox="0 0 16 28"><path d="M3 2l10 12L3 26" fill="none" stroke="#777" stroke-width="4"/></svg>

<h2 class="section-title abs">Our Products</h2>
<div class="decal-ad abs"><div class="inner"><span class="name">Brisk Tide</span><span class="word">DECALS</span><span class="cta">GET NOW</span></div></div>
<div class="product abs" style="left:371px;width:207px"><div class="shot" role="img" aria-label="Yellow sword shirt, back and front" style="background:linear-gradient(#f6ee9a,#e9df7d)"></div><h3>Sword Shirt</h3><div class="price">$19.99</div><span class="buy">BUY NOW</span></div>
<div class="product abs" style="left:581px;width:203px"><div class="shot" role="img" aria-label="White trout shirt, back and front" style="background:linear-gradient(#f4f4f4,#d9e6e6)"></div><h3>Trout Shirt White</h3><div class="price">$18.99</div><span class="buy">BUY NOW</span></div>
<div class="product abs" style="left:786px;width:212px"><div class="shot" role="img" aria-label="Black logo shirt, back and front" style="background:linear-gradient(#2e2820,#17130f)"></div><h3>Logo Shirt</h3><div class="price">$20.99</div><span class="buy">BUY NOW</span></div>

<h2 class="welcome-title abs">Welcome to Brisk Tide</h2>
<p class="welcome-text abs">This is Layoutkit's version &nbsp;of Lorem Ipsum. Proin gravida nibh vel velit auctor aliquet. Aenean sollicitudin, lorem quis bibendum auctor, nisi elit consequat ipsum, nec sagittis sem nibh id elit. Duis sed odio sit amet nibh vulputate cursus a sit amet mauris. Morbi accumsan ipsum velit. Nam nec tellus a odio tincidunt auctor a ornare odio. Sed non &nbsp;mauris vitae erat consequat auctor eu in elit. Class aptent taciti sociosqu ad litora torquent per conubia nostra, per inceptos himenaeos. Mauris in erat justo. Nullam ac urna eu felis dapibus condimentum sit amet a augue.</p>

<h2 class="news-title abs">Newsletter Signup</h2>
<div class="news-form abs"><span>Your e-mail id</span><b>SIGNUP</b></div>
<h2 class="follow-title abs">Follow Us</h2>
<div class="social abs" style="left:588px"><i style="background:#3b5a98"></i>Like our page</div>
<div class="social abs" style="left:752px"><i style="background:#3fb5e8"></i>Follow Us</div>
<div class="social abs" style="left:886px"><i style="background:#d8344a"></i>Follow Us</div>

<footer class="footer abs"></footer>
<nav class="foot-links abs" style="top:1136px"><span>HOME</span>|<span>COLLECTIONS</span>|<span>SHIRTS</span>|<span>SHORTS</span>|<span>HEADWEAR</span>|<span>DECALS</span>|<span style="font-weight:400">CONTACT US</span>|<span style="font-weight:400">SIGNUP</span>|</nav>
<nav class="foot-links abs" style="top:1165px;font-weight:400;gap:14px"><span>MY ACCOUNT</span><span>CREATE ACCOUNT</span><span>TRACK</span><span>MY ORDER</span><span>FAQ</span><span>TERMS</span></nav>
<div class="foot-brand abs">Brisk Tide</div>
<div class="copy abs">©2013</div>
</body>
</html>
```